Design Business Cards for my forest, wood company

Hi ,
I need that you create Business Card and for my forest, wood company
display on it Name Surname , job position(Director) , the type of work we do (logging ,woodworking) ,
telephone number , email ,
and our adress with bank account which is written togehter in 4 rows
example for adress and bank account it has to be together ,
Reg.Nr. 718290537
Pilvena Mustod Ka
Toliksa Brevins LE-8715
KVP LE71MOTR0004817566

Suggested colors are Green , yellow , black , brown

also you need to add,create nice looking and simple logo with my bussines name which has some kind of icon or symbol, picture . I add logo example what I want in it , three icons in one there is trees , in other there is wood planks and in third ear field .
My company name "ĶIRBĒLU DOMASTES"

I add my bussines name in picture format , because it includes signs which are not in english.
I add Business card example which I like , it has everything I mentioned .

If any question please ask , if I will see business card which I like will award it immediately .

```html
<!DOCTYPE html>
<html lang="lv">
<head>
<meta charset="utf-8">
<title>Ķirbēlu Domastes — Business Card</title>
<link href="https://fonts.googleapis.com/css2?family=Jost:wght@400;500;600&display=swap" rel="stylesheet">
<style>
  :root {
    --page: #ffffff;
    --bark: #3d2412;
    --canopy: #5a3b1f;
    --canopy-soft: rgba(90, 59, 31, 0);
    --leaf: #8cc63e;
    --cream: #f1d7a6;
    --sand: #d9c3a0;
  }
  * { margin: 0; padding: 0; box-sizing: border-box; }
  html, body {
    width: 1200px; height: 535px; overflow: hidden;
    background: var(--page);
    font-family: "Jost", "Century Gothic", sans-serif;
  }
  .card {
    position: absolute;
    width: 356px; height: 203px;
    background: var(--bark);
    overflow: hidden;
  }
  .card--front { left: 201px; top: 168px; }
  .card--back  { left: 680px; top: 167px; }

  .tree-art {
    position: absolute;
    background: radial-gradient(ellipse at 50% 45%, var(--canopy) 55%, var(--canopy-soft) 72%);
  }
  .card--front .tree-art { left: 10px; top: -20px; width: 336px; height: 160px; }
  .card--back .tree-art { left: 165px; top: 8px; width: 190px; height: 140px; }

  .grass-art {
    position: absolute; left: 80px; top: 166px; width: 206px; height: 37px;
    background: linear-gradient(to top, var(--canopy), var(--canopy-soft));
  }

  .mark {
    position: absolute;
    border: 2px solid var(--leaf);
  }
  .card--front .mark { left: 157px; top: 53px; width: 46px; height: 46px; }
  .card--back .mark  { left: 60px; top: 29px; width: 44px; height: 43px; }

  .brand-name {
    position: absolute;
    color: var(--cream);
    font-weight: 500;
    font-size: 14px;
    letter-spacing: 0.5px;
    white-space: nowrap;
    text-align: center;
  }
  .card--front .brand-name { left: 0; width: 356px; top: 104px; }
  .card--back .brand-name  { left: 12px; width: 148px; top: 80px; font-size: 13px; }

  .rule { position: absolute; height: 1px; background: var(--sand); }
  .card--front .rule { left: 108px; width: 143px; top: 127px; }
  .card--back .rule  { left: 20px; width: 131px; top: 100px; }

  .tagline {
    position: absolute;
    color: var(--sand);
    font-size: 9px;
    text-align: center;
    white-space: nowrap;
  }
  .card--front .tagline { left: 0; width: 356px; top: 131px; }
  .card--back .tagline  { left: 12px; width: 148px; top: 102px; }

  .person { position: absolute; left: 217px; top: 39px; color: var(--sand); }
  .person__name { font-size: 12.5px; line-height: 1.1; }
  .person__role { font-size: 10.5px; margin-left: 3px; }

  .accent-line { position: absolute; left: 163px; top: 107px; width: 174px; height: 1px; background: var(--leaf); }
  .accent-bar  { position: absolute; left: 300px; top: 106px; width: 37px; height: 3px; background: var(--leaf); }

  .contacts { position: absolute; left: 20px; top: 135px; list-style: none; }
  .contacts li {
    display: flex; align-items: center; gap: 7px;
    height: 19px; font-size: 9px; color: var(--sand);
  }
  .contacts svg { width: 8px; height: 10px; fill: var(--leaf); flex: none; }

  .divider { position: absolute; left: 157px; top: 134px; width: 1px; height: 56px; background: var(--leaf); }

  .company-details {
    position: absolute; left: 216px; top: 136px;
    font-size: 9px; line-height: 13.5px; color: var(--sand);
    font-style: normal; white-space: nowrap;
  }
</style>
</head>
<body>

<section class="card card--front" aria-label="Card front">
  <div class="tree-art" role="img" aria-label="Faint silhouette of a large broad-leaf tree"></div>
  <div class="grass-art" role="img" aria-label="Faint grass silhouette along the bottom edge"></div>
  <div class="mark"></div>
  <div class="brand-name">ĶIRBĒLU DOMASTES</div>
  <div class="rule"></div>
  <div class="tagline">Logging &amp; Woodworking</div>
</section>

<section class="card card--back" aria-label="Card back">
  <div class="tree-art" role="img" aria-label="Faint silhouette of a broad-leaf tree"></div>
  <div class="mark"></div>
  <div class="brand-name">ĶIRBĒLU DOMASTES</div>
  <div class="rule"></div>
  <div class="tagline">Logging &amp; Woodworking</div>

  <div class="person">
    <div class="person__name">Name Surname</div>
    <div class="person__role">Director</div>
  </div>
  <div class="accent-line"></div>
  <div class="accent-bar"></div>

  <ul class="contacts">
    <li><svg viewBox="0 0 8 10"><rect x="1" y="0" width="6" height="10" rx="1.2"/><rect x="2" y="1.5" width="4" height="5" fill="#3d2412"/></svg>01-004-7821</li>
    <li><svg viewBox="0 0 8 10"><rect x="1" y="0" width="6" height="10" rx="1.2"/><rect x="2" y="1.5" width="4" height="5" fill="#3d2412"/></svg>01-004-5560</li>
    <li><svg viewBox="0 0 8 10"><rect x="0" y="2.5" width="8" height="5.5"/><path d="M0 2.5 L4 5.5 L8 2.5" stroke="#3d2412" stroke-width="0.8" fill="none"/></svg>name@email.com</li>
  </ul>

  <div class="divider"></div>

  <address class="company-details">
    Reg.Nr. 718290537<br>
    Pilvena Mustod Ka<br>
    Toliksa Brevins LE-8715<br>
    KVP LE71MOTR0004817566
  </address>
</section>

</body>
</html>
```